Harborline Energy - needs a business card

Harborline Energy is a U.S. based diesel sourcing and distribution company that supports American oil & gas fields through providing quality product and consistent services.

Target Market(s)

Oil and Gas

Contact Information for Business Card

The background of the card must be white to ensure the logo pops.

Font styles to use
Serif
Sans Serif

Colors

Designer to choose colors to be used in the design.

Requirements
Must have
• Front of Card: Tag line: Harborline Energy, Powering America's Oil & Gas fields.
• Not sure if you guys do this part but just in case...
• Dale Menschow
• Owner/CEO
• C:555.318.4076
• E:Dmenschow@harborlineenergy.example
• W:Harborlineenergy.example
• Locations: Servicing the Powder River, DJ basin and Bakken formations.
• Back of Card: " Frac fueling is what we do. We understand how important diesel fuel is to your operation, which is why our main service line is Frac fueling. We assure our supply and stand by our service"

```html
<!DOCTYPE html>
<html lang="en">
<head>
<meta charset="utf-8">
<title>Harborline Energy – Business Card</title>
<link rel="stylesheet" href="https://fonts.googleapis.com/css2?family=Open+Sans:wght@400;600;700;800&display=swap">
<style>
  :root {
    --navy: #11306b;
    --red: #c1121f;
    --grey: #6b6b6b;
    --paper: #ffffff;
    --backdrop: #e4e5e8;
  }
  * { box-sizing: border-box; margin: 0; padding: 0; }
  html, body { width: 1200px; height: 892px; overflow: hidden; }
  body {
    background: var(--backdrop);
    font-family: "Open Sans", Arial, sans-serif;
    position: relative;
  }
  .card {
    position: absolute;
    left: 250px;
    width: 700px;
    height: 400px;
    background: var(--paper);
    box-shadow: 0 6px 18px rgba(0,0,0,0.18);
    overflow: hidden;
  }
  .card--back { top: 30px; }
  .card--front { top: 462px; }

  /* Back */
  .back-brand {
    position: absolute;
    top: 140px; left: 0; right: 0;
    display: flex; align-items: center; justify-content: center; gap: 12px;
  }
  .brand-dot {
    width: 18px; height: 18px; border-radius: 50%;
    background: var(--red);
  }
  .brand-name {
    font-weight: 800;
    color: var(--navy);
    letter-spacing: 0.5px;
  }
  .back-brand .brand-name { font-size: 40px; }
  .back-statement {
    position: absolute;
    left: 60px; right: 60px; bottom: 40px;
    text-align: center;
    font-size: 13px;
    line-height: 1.5;
    color: var(--grey);
  }

  /* Front */
  .front-panel { position: absolute; inset: 0; }
  .front-brand {
    position: absolute; top: 52px; left: 40px;
    display: flex; align-items: center; gap: 10px;
  }
  .front-brand .brand-name { font-size: 32px; }
  .person { position: absolute; top: 132px; left: 40px; }
  .person-name { font-size: 22px; font-weight: 700; color: var(--navy); line-height: 1.2; }
  .person-role { font-size: 17px; color: var(--red); line-height: 1.3; }
  .service-area {
    margin-top: 6px;
    font-size: 17px; color: var(--grey); line-height: 1.3;
  }
  .contact-list { list-style: none; margin-top: 10px; }
  .contact-item {
    display: flex; align-items: center; gap: 10px;
    font-size: 16px; color: var(--grey); line-height: 1.55;
  }
  .contact-icon { width: 16px; height: 16px; flex: none; }
  .tagline {
    margin-top: 10px;
    font-size: 16px; font-weight: 700; color: var(--navy); line-height: 1.3;
    width: 360px;
  }
</style>
</head>
<body>

  <section class="card card--back" aria-label="Back of business card">
    <div class="back-brand">
      <span class="brand-dot"></span>
      <span class="brand-name">Harborline Energy</span>
    </div>
    <p class="back-statement">Frac fueling is what we do. We understand how important diesel fuel is to your operation, which is why our main service line is Frac fueling. We assure our supply and stand by our service</p>
  </section>

  <section class="card card--front" aria-label="Front of business card">
    <svg class="front-panel" viewBox="0 0 700 400" width="700" height="400" aria-hidden="true">
      <path d="M400,0 L700,0 L700,400 L640,400 C690,290 560,130 400,0 Z" fill="var(--navy)"/>
    </svg>

    <div class="front-brand">
      <span class="brand-dot"></span>
      <span class="brand-name">Harborline Energy</span>
    </div>

    <div class="person">
      <p class="person-name">Dale Menschow</p>
      <p class="person-role">Owner/CEO</p>
      <p class="service-area">Servicing the Powder River<br>DJ basin &amp; Bakken formations.</p>

      <ul class="contact-list">
        <li class="contact-item">
          <svg class="contact-icon" viewBox="0 0 16 16" aria-hidden="true">
            <rect x="4" y="1" width="8" height="14" rx="1.5" fill="none" stroke="var(--navy)" stroke-width="1.8"/>
            <circle cx="8" cy="12.3" r="0.9" fill="var(--navy)"/>
          </svg>
          555.318.4076
        </li>
        <li class="contact-item">
          <svg class="contact-icon" viewBox="0 0 16 16" aria-hidden="true">
            <rect x="1" y="3" width="14" height="10" fill="var(--navy)"/>
            <path d="M1,3 L8,9 L15,3" fill="none" stroke="#fff" stroke-width="1.3"/>
          </svg>
          Dmenschow@harborlineenergy.example
        </li>
        <li class="contact-item">
          <svg class="contact-icon" viewBox="0 0 16 16" aria-hidden="true">
            <circle cx="8" cy="8" r="7" fill="var(--navy)"/>
            <path d="M1,8 H15 M8,1 C4.5,5 4.5,11 8,15 M8,1 C11.5,5 11.5,11 8,15" fill="none" stroke="#fff" stroke-width="1"/>
          </svg>
          www.Harborlineenergy.example
        </li>
      </ul>

      <p class="tagline">Harborline Energy, Powering America's Oil &amp; Gas fields.</p>
    </div>
  </section>

</body>
</html>
```